Homepage Real Estate Agency

I need a web design for a real estate agency in Luxembourg. A short draft for the front page can be found in the project details. (Page 1+2) The main colors of the site should be blue as shown in the project details. (Page 3)
The main target for this site is to promote real estates and a small presentation of the company.

Industry/Entity Type

Real Estate

Requirements
Must have
• On the front page estates are shown in a short preview in small boxes, on the right side is a search. The search is hidden except for the front page. The header has 4 buttons and the logo of the company.

```html
<!DOCTYPE html>
<html lang="fr">
<head>
<meta charset="utf-8">
<title>Valmont Immo – Accueil</title>
<link rel="stylesheet" href="https://fonts.googleapis.com/css2?family=Yanone+Kaffeesatz:wght@300;400&family=Open+Sans:wght@400;600&display=swap">
<style>
:root{
  --navy:#0d3a8c;
  --blue:#1a58b0;
  --blue-light:#2f70c4;
  --band-dark:#0f4596;
  --band-mid:#2566bd;
  --red:#d10f14;
  --red-dark:#a80a0e;
  --grey-text:#555;
  --white:#fff;
  --head:"Yanone Kaffeesatz",sans-serif;
  --body:"Open Sans",sans-serif;
}
*{box-sizing:border-box;margin:0;padding:0}
html,body{width:1059px;height:1200px;overflow:hidden}
body{position:relative;background:var(--white);font-family:var(--body);color:var(--grey-text)}
.abs{position:absolute}

/* header */
.topline{left:0;top:0;width:1059px;height:9px;background:var(--navy)}
.header{left:0;top:9px;width:1059px;height:134px;background:linear-gradient(#d9d9d9,#f4f4f4 55%,#fff)}
.brand-tab{left:106px;top:0;width:163px;height:141px;background:linear-gradient(#fff,#e2e2e2);border-radius:0 0 26px 14px;box-shadow:0 2px 4px rgba(0,0,0,.25);display:flex;flex-direction:column;align-items:center;justify-content:center;gap:8px}
.brand-dot{width:22px;height:22px;border-radius:50%;background:var(--navy)}
.brand-name{font-family:var(--head);font-weight:400;font-size:28px;color:var(--navy);line-height:1}
.account{right:109px;top:17px;font-size:11px;color:#777}
.nav{right:110px;top:49px;display:flex;align-items:center;height:34px}
.nav a{font-family:var(--head);font-weight:300;font-size:24px;color:#555;text-decoration:none;margin-left:20px;line-height:34px}
.nav a.current{background:linear-gradient(var(--blue-light),var(--navy));color:#fff;padding:0 19px;border-radius:3px;margin-left:0;margin-right:-12px}

/* slider */
.band{left:0;top:143px;width:1059px;height:274px;background:linear-gradient(90deg,var(--band-dark),var(--band-mid) 50%,var(--band-dark))}
.slider{left:119px;top:154px;width:821px;height:270px;background:#fff;border:1px solid #ddd;padding:6px 7px}
.slide-photo{width:100%;height:100%;background:linear-gradient(160deg,#e9b36a,#b8642f 45%,#3a2412 85%)}
.shadow{left:130px;top:424px;width:800px;height:18px;background:radial-gradient(ellipse at top,rgba(0,0,0,.2),transparent 70%)}
.arrow{top:254px}

/* panels */
.panel{background:linear-gradient(90deg,var(--navy),var(--blue) 60%,var(--blue-light))}
.panel-title{font-family:var(--head);font-weight:400;font-size:24px;color:#fff;position:absolute;left:13px;top:8px}
.panel-rule{position:absolute;left:12px;right:10px;border-top:1px dotted rgba(255,255,255,.45)}
.featured{left:106px;top:455px;width:581px;height:331px}
.offer{position:absolute;top:53px;width:165px;color:#fff}
.frame{border:1px solid #fff;padding:6px;background:var(--white);outline:2px solid rgba(255,255,255,.3)}
.frame .pic{width:100%;height:100%;background:linear-gradient(#cfe0ea,#7d8a66 55%,#3f5a2c)}
.offer .frame{height:148px}
.offer .name{font-size:13px;line-height:18px;margin:6px 0 0 3px}
.offer .price{font-size:13px;line-height:18px;margin:0 0 0 3px}
.offer .price span{color:var(--red)}
.offer .desc{font-size:11px;line-height:14px;margin:5px 0 0 3px}
.btn-details{display:block;width:86px;height:22px;margin:12px 0 0 3px;border:2px solid #fff;border-radius:3px 11px 11px 3px;background:linear-gradient(#e62a2a,var(--red-dark));color:#fff;font-size:11px;line-height:18px;padding-left:24px;position:relative}
.btn-details::after{content:"";position:absolute;right:4px;top:5px;width:8px;height:8px;border-radius:50%;background:#fff}

/* search */
.search{left:699px;top:455px;width:254px;height:331px;border:1px solid #ccc;padding:4px}
.search-inner{position:relative;width:100%;height:100%;background:#e4e4e4}
.search h2{position:absolute;left:9px;top:6px;font-family:var(--head);font-weight:300;font-size:25px;color:#555}
.search .rule{position:absolute;left:9px;right:8px;top:39px;border-top:1px solid #fff}
.lbl{position:absolute;font-size:11px;line-height:14px;color:#555}
.field{position:absolute;height:19px;background:#fff;border:1px solid #bbb;font-size:11px;color:#555;line-height:17px;padding-left:7px}
.sel::after{content:"";position:absolute;right:1px;top:1px;width:15px;height:15px;background:linear-gradient(#7cc4f0,#2d8fd4)}
.sel::before{content:"";position:absolute;right:5px;top:7px;z-index:1;border:4px solid transparent;border-top:4px solid #fff}
.btn-search{position:absolute;left:112px;top:265px;width:122px;height:28px;border-radius:5px 14px 14px 5px;background:linear-gradient(#e62a2a,var(--red-dark));color:#fff;font-size:12px;line-height:28px;padding-left:7px;white-space:nowrap}
.btn-search::after{content:"›";position:absolute;right:4px;top:5px;width:18px;height:18px;border-radius:50%;background:#bbb;color:#fff;font-size:14px;line-height:17px;text-align:center}
.hint{position:absolute;left:8px;top:296px;font-size:10px;line-height:11px;color:#666}

/* gallery */
.gallery{left:106px;top:807px;width:847px;height:225px}
.thumb{position:absolute;top:68px;width:139px;height:122px}

/* footer */
.foot-line{left:0;top:1041px;width:1059px;height:9px;background:var(--navy)}
.footer{left:0;top:1050px;width:1059px;height:150px;background:linear-gradient(#d6d6d6,#f7f7f7 60%,#fff)}
.foot-title{font-family:var(--head);font-weight:300;font-size:24px;color:#555}
.locality{top:1090px}
.locality h3{font-size:13px;font-weight:400;color:var(--red);margin-bottom:5px}
.locality li,.links li{list-style:none;font-size:11px;line-height:14.4px;color:#666}
.divider{left:673px;top:1055px;height:128px;border-left:1px solid #aaa}
.social{top:1086px;width:26px;height:26px;border-radius:4px;background:linear-gradient(#3b75c4,#1b4a93)}
.copy{left:692px;top:1183px;font-size:10px;color:var(--red)}
</style>
</head>
<body>
<div class="abs topline"></div>
<header class="abs header"></header>
<div class="abs brand-tab"><span class="brand-dot"></span><span class="brand-name">Valmont Immo</span></div>
<div class="abs account">Login | Signup</div>
<nav class="abs nav">
  <a class="current" href="#">HOME</a><a href="#">A VENDRE</a><a href="#">CONSTRUCTION</a><a href="#">LOCATION</a><a href="#">CHERCHONS</a>
</nav>

<div class="abs band"></div>
<div class="abs slider"><div class="slide-photo" role="img" aria-label="Large villa with balconies at sunset"></div></div>
<div class="abs shadow"></div>
<svg class="abs arrow" style="left:118px" width="42" height="78" viewBox="0 0 42 78"><path d="M0 0A39 39 0 0 1 0 78Z" fill="#1d54ac" stroke="#fff" stroke-width="1"/><path d="M22 31l-8 8 8 8" fill="none" stroke="#d10f14" stroke-width="4"/></svg>
<svg class="abs arrow" style="left:899px" width="42" height="78" viewBox="0 0 42 78"><path d="M42 0A39 39 0 0 0 42 78Z" fill="#1d54ac" stroke="#fff" stroke-width="1"/><path d="M20 31l8 8-8 8" fill="none" stroke="#d10f14" stroke-width="4"/></svg>

<section class="abs panel featured">
  <h2 class="panel-title">Featured Offers</h2>
  <div class="panel-rule" style="top:40px"></div>
  <article class="offer" style="left:10px">
    <div class="frame"><div class="pic" role="img" aria-label="Blue bungalow with white picket fence"></div></div>
    <p class="name">sample text</p><p class="price">Price: <span>0000000</span></p>
    <p class="desc">sample text sample text<br>sample text sample text<br>sample text sample text</p>
    <span class="btn-details">Details</span>
  </article>
  <article class="offer" style="left:208px">
    <div class="frame"><div class="pic" role="img" aria-label="Yellow two-storey house with trees"></div></div>
    <p class="name">sample text</p><p class="price">Price: <span>0000000</span></p>
    <p class="desc">sample text sample text<br>sample text sample text<br>sample text sample text</p>
    <span class="btn-details">Details</span>
  </article>
  <article class="offer" style="left:406px">
    <div class="frame"><div class="pic" role="img" aria-label="Cottage with flower garden"></div></div>
    <p class="name">sample text</p><p class="price">Price: <span>0000000</span></p>
    <p class="desc">sample text sample text<br>sample text sample text<br>sample text sample text</p>
    <span class="btn-details">Details</span>
  </article>
</section>

<aside class="abs search">
  <div class="search-inner">
    <h2>Find Your Property</h2><div class="rule"></div>
    <span class="lbl" style="left:8px;top:42px">City:</span>
    <span class="lbl" style="left:136px;top:42px">State:</span>
    <div class="field" style="left:8px;top:61px;width:99px"></div>
    <div class="field" style="left:136px;top:61px;width:99px"></div>
    <span class="lbl" style="left:11px;top:86px">Zip:</span>
    <span class="lbl" style="left:136px;top:86px">Country:</span>
    <div class="field" style="left:8px;top:105px;width:102px"></div>
    <div class="field" style="left:136px;top:105px;width:99px"></div>
    <span class="lbl" style="left:11px;top:130px">Price Range:</span>
    <div class="field sel" style="left:11px;top:148px;width:97px">Max</div>
    <span class="lbl" style="left:114px;top:151px">To:</span>
    <div class="field sel" style="left:136px;top:148px;width:99px">Min</div>
    <span class="lbl" style="left:11px;top:175px">Bedroom:</span>
    <div class="field sel" style="left:11px;top:194px;width:224px"></div>
    <span class="lbl" style="left:11px;top:219px">Bathroom:</span>
    <div class="field sel" style="left:11px;top:237px;width:224px"></div>
    <span class="btn-search">Search Property</span>
    <p class="hint">Know exactly what you want?<br>Advanced search</p>
  </div>
</aside>

<section class="abs panel gallery">
  <h2 class="panel-title">Project Gallery</h2>
  <div class="panel-rule" style="top:42px"></div>
  <div class="frame thumb" style="left:10px"><div class="pic" role="img" aria-label="Blue bungalow"></div></div>
  <div class="frame thumb" style="left:179px"><div class="pic" role="img" aria-label="White gabled house"></div></div>
  <div class="frame thumb" style="left:355px"><div class="pic" role="img" aria-label="Brick cottage with chimney"></div></div>
  <div class="frame thumb" style="left:525px"><div class="pic" role="img" aria-label="Street of family houses"></div></div>
  <div class="frame thumb" style="left:695px"><div class="pic" role="img" aria-label="Beige two-storey house"></div></div>
</section>

<div class="abs foot-line"></div>
<footer class="abs footer"></footer>
<h2 class="abs foot-title" style="left:108px;top:1052px">Browse Propery by Locality</h2>
<ul class="abs locality" style="left:108px"><h3>Country Name</h3><li>sample link</li><li>sample link</li><li>sample link</li><li>sample link</li><li>sample link</li></ul>
<ul class="abs locality" style="left:229px"><h3>Country Name</h3><li>sample link</li><li>sample link</li><li>sample link</li><li>sample link</li><li>sample link</li></ul>
<ul class="abs locality" style="left:345px"><h3>Country Name</h3><li>sample link</li><li>sample link</li><li>sample link</li><li>sample link</li><li>sample link</li></ul>
<ul class="abs locality" style="left:456px"><h3>Country Name</h3><li>sample link</li><li>sample link</li><li>sample link</li><li>sample link</li><li>sample link</li></ul>
<ul class="abs locality" style="left:574px"><h3>Country Name</h3><li>sample link</li><li>sample link</li><li>sample link</li><li>sample link</li><li>sample link</li></ul>
<div class="abs divider"></div>
<h2 class="abs foot-title" style="left:692px;top:1051px">Links</h2>
<ul class="abs links" style="left:692px;top:1080px"><li>Home</li><li>About Us</li><li>A Vendre</li><li>Construction</li><li>Location</li><li>Cherchons</li><li>Contact Us</li></ul>
<h2 class="abs foot-title" style="left:837px;top:1051px">Follow Us</h2>
<span class="abs social" style="left:836px"></span>
<span class="abs social" style="left:874px"></span>
<span class="abs social" style="left:910px"></span>
<p class="abs copy">© copyright 2012 by Real estate all rights reserved.</p>
</body>
</html>
```